Baby Care Print Log for Nannies and Parents- Creating a brand/style I can use across different forms

I am creating a notebook for babysitters to use to communicate with parents about the children they care for. I will be creating many different forms (emergency contacts, daily logs, shopping lists, etc.)
I need a look and feel from which to style these forms from. I am starting by designing the daily baby care log. I need a designer to take my Word doc with just text on it, and create a visual approach to make this visually appealing.
I do not want this to be extremely "babyish" with cartoon styling. I want it to be more of a professional looking style. I would like to be able to color each different document a different color palette, yet keep the similar look and feel. My logo is attached for inspiration. I use real photography across my website velmorapath.com.
Updates
I will be re-designing my Wordpress website based on what design I like best and also will need other forms completed once I pick a design. I am hoping to work with someone who I can hire for further development needs as well. Added Saturday, February 11, 2017
Target Market(s)
Professional Parents
Industry/Entity Type
Education
Requirements
Must have
- color, pop, visual appeal
- Please use the color in my logo and any complementary colors that you think work well with it. I definitely like colored patterns, ombre, colored backgrounds, etc. I'd prefer for it not to be completely white with only pops of color here and there.
Nice to have
- My logo somewhere subtly on the form
- Photography elements
Should not have
- cartoon images of babies, etc. I use real photography across my website with the exception of my logo umbrella.

```html
<!DOCTYPE html>
<html lang="en">
<head>
<meta charset="utf-8">
<title>Velmora Path – Daily Baby Care Log</title>
<link rel="stylesheet" href="https://fonts.googleapis.com/css2?family=Questrial&display=swap">
<style>
  :root{
    --nap:#0cb7d9;
    --feed:#9bc93d;
    --diaper:#f07124;
    --mood:#e4449a;
    --ink:#1d1d1f;
    --sky-top:#ffffff;
    --sky-mid:#6fd0f6;
    --sky-deep:#0aaaf0;
    --sky-low:#17a6e4;
    --stage:#e6e7ea;
  }
  *{box-sizing:border-box;margin:0;padding:0}
  html,body{width:1200px;height:1200px;overflow:hidden;background:var(--stage)}
  body{font-family:"Questrial",sans-serif;color:var(--ink)}
  .log-page{
    position:absolute;left:176px;top:0;width:848px;height:1200px;
    background:linear-gradient(to bottom,var(--sky-top) 0,var(--sky-top) 150px,#cdeefb 300px,var(--sky-mid) 470px,var(--sky-deep) 720px,var(--sky-low) 1200px);
    overflow:hidden;
  }
  .brand{position:absolute;top:82px;left:0;width:100%;display:flex;justify-content:center;align-items:center;gap:14px}
  .brand-dot{width:22px;height:22px;border-radius:50%;background:var(--nap)}
  .brand-name{font-size:46px;color:var(--ink);letter-spacing:1px}
  .field{position:absolute;top:186px;font-size:20px;display:flex;align-items:flex-end}
  .field-line{display:inline-block;border-bottom:1.5px solid var(--ink);margin-left:6px;height:22px}
  .card{
    position:absolute;background:#fff;border:1.5px solid var(--accent);
    border-bottom:11px solid var(--accent);border-radius:10px;
  }
  .tab{
    position:absolute;background:var(--accent);color:#fff;border-radius:10px;
    display:flex;align-items:center;justify-content:center;font-size:18px;
  }
  .nap{--accent:var(--nap)} .feed{--accent:var(--feed)}
  .diaper{--accent:var(--diaper)} .mood{--accent:var(--mood)}
  .label{position:absolute;font-size:18px}
  .rule{position:absolute;border-bottom:1.5px solid var(--ink)}
  .box{position:absolute;width:20px;height:20px;border:1.5px solid #333;background:#fff}
  .check{position:absolute;display:flex;align-items:center;gap:12px;font-size:18px}
  .check::before{content:"";width:14px;height:14px;border:1.5px solid #444}
  .supply{font-size:13.5px;gap:10px}
  .supply::before{width:12px;height:12px}
  .site-band{
    position:absolute;left:0;top:1120px;width:100%;height:42px;background:var(--diaper);
    color:#fff;font-size:19px;letter-spacing:3px;display:flex;align-items:center;justify-content:center;
  }
</style>
</head>
<body>
<main class="log-page">
  <header class="brand">
    <span class="brand-dot"></span>
    <span class="brand-name">Velmora Path</span>
  </header>

  <div class="field" style="left:97px">Name<span class="field-line" style="width:236px"></span></div>
  <div class="field" style="left:454px">Date<span class="field-line" style="width:245px"></span></div>

  <!-- Nap time -->
  <section class="card nap" style="left:97px;top:251px;width:297px;height:198px">
    <span class="label" style="left:27px;top:35px">Time</span>
    <span class="label" style="left:154px;top:35px">How Long</span>
    <span class="rule" style="left:27px;top:84px;width:54px"></span><span class="rule" style="left:123px;top:84px;width:140px"></span>
    <span class="rule" style="left:27px;top:114px;width:54px"></span><span class="rule" style="left:123px;top:114px;width:140px"></span>
    <span class="rule" style="left:27px;top:144px;width:54px"></span><span class="rule" style="left:123px;top:144px;width:140px"></span>
    <span class="rule" style="left:27px;top:174px;width:54px"></span><span class="rule" style="left:123px;top:174px;width:140px"></span>
  </section>
  <div class="tab nap" style="left:125px;top:233px;width:239px;height:40px">NAP TIME</div>

  <!-- Feeding -->
  <section class="card feed" style="left:454px;top:251px;width:297px;height:198px">
    <span class="label" style="left:27px;top:35px">Time</span>
    <span class="label" style="left:167px;top:35px">What</span>
    <span class="rule" style="left:27px;top:84px;width:54px"></span><span class="rule" style="left:123px;top:84px;width:140px"></span>
    <span class="rule" style="left:27px;top:114px;width:54px"></span><span class="rule" style="left:123px;top:114px;width:140px"></span>
    <span class="rule" style="left:27px;top:144px;width:54px"></span><span class="rule" style="left:123px;top:144px;width:140px"></span>
    <span class="rule" style="left:27px;top:174px;width:54px"></span><span class="rule" style="left:123px;top:174px;width:140px"></span>
  </section>
  <div class="tab feed" style="left:483px;top:233px;width:239px;height:40px">FEEDING</div>

  <!-- Diapers -->
  <section class="card diaper" style="left:97px;top:486px;width:297px;height:198px">
    <span class="label" style="left:27px;top:35px">Time</span>
    <span class="label" style="left:141px;top:35px">Wet</span>
    <span class="label" style="left:217px;top:35px">BM</span>
    <span class="rule" style="left:27px;top:84px;width:54px"></span><span class="box" style="left:146px;top:66px"></span><span class="box" style="left:219px;top:66px"></span>
    <span class="rule" style="left:27px;top:114px;width:54px"></span><span class="box" style="left:146px;top:96px"></span><span class="box" style="left:219px;top:96px"></span>
    <span class="rule" style="left:27px;top:144px;width:54px"></span><span class="box" style="left:146px;top:126px"></span><span class="box" style="left:219px;top:126px"></span>
    <span class="rule" style="left:27px;top:173px;width:54px"></span><span class="box" style="left:146px;top:155px"></span><span class="box" style="left:219px;top:155px"></span>
  </section>
  <div class="tab diaper" style="left:125px;top:468px;width:239px;height:40px">DIAPERS</div>

  <!-- Mood -->
  <section class="card mood" style="left:454px;top:486px;width:297px;height:198px">
    <span class="check" style="left:27px;top:34px">Happy</span>
    <span class="check" style="left:27px;top:63px">Sad</span>
    <span class="check" style="left:27px;top:93px">Unsettled</span>
    <span class="check" style="left:27px;top:123px">Energetic</span>
    <span class="check" style="left:27px;top:152px">Tired</span>
    <span class="check" style="left:170px;top:34px">Chatty</span>
    <span class="check" style="left:170px;top:63px">Quiet</span>
  </section>
  <div class="tab mood" style="left:483px;top:468px;width:239px;height:40px">MOOD</div>

  <!-- Today's activities -->
  <section class="card mood" style="left:97px;top:716px;width:654px;height:112px;border-bottom-width:6px"></section>
  <div class="tab mood" style="left:300px;top:701px;width:239px;height:31px">Today’s Activities</div>

  <!-- Supplies -->
  <section class="card diaper" style="left:97px;top:852px;width:654px;height:111px;border-bottom-width:6px">
    <span class="check supply" style="left:51px;top:34px">Diapers</span>
    <span class="check supply" style="left:51px;top:54px">Diaper Cream</span>
    <span class="check supply" style="left:51px;top:74px">Other:</span>
    <span class="check supply" style="left:246px;top:34px">Milk/Formula</span>
    <span class="check supply" style="left:246px;top:54px">Cereal</span>
    <span class="check supply" style="left:482px;top:34px">Wet Wipes</span>
    <span class="check supply" style="left:482px;top:54px">Baby Food</span>
  </section>
  <div class="tab diaper" style="left:300px;top:838px;width:239px;height:30px">Supplies Needed Soon</div>

  <!-- Special notes -->
  <section class="card feed" style="left:97px;top:988px;width:654px;height:112px;border-bottom-width:6px">
    <span class="rule" style="left:27px;top:44px;width:596px"></span>
    <span class="rule" style="left:27px;top:65px;width:596px"></span>
    <span class="rule" style="left:27px;top:86px;width:596px"></span>
  </section>
  <div class="tab feed" style="left:300px;top:973px;width:239px;height:31px">Special Notes</div>

  <footer class="site-band">www.velmorapath.com</footer>
</main>
</body>
</html>
```